Motivational Poster Series for Students at Truck Driving School

We are looking for a series of 3 motivational posters (18"X 24") to be used in classrooms at a truck driving school. The audience for the posters will be the students that are currently in school and the purpose of the posters is to be motivational pieces that will be displayed on the walls.

We have provided the quotes below that are to be used on each poster. We have also provided some example images from PixVaultImages to give an idea on the backgrounds that we'd like to see on each poster. The images do not have to be exact, these are just examples of what we think will look good for each quote. Since this is a series, they can all be somewhat similar in look/feel - just with different images and quotes.

So, the basic idea is a background image/design with a quote being the main point of emphasis. Other than that, we would like to include the logo provided at a small scale in one of the corners of the poster as a watermark for branding purposes.

Below are the quotes for each of the 3 posters:

Poster 1 - “It’s very difficult to follow our dreams, but it’s even more difficult to forget them.” - Devan Okafor

Poster 2 - “Success doesn’t just come and find you, you have to go out and get it.” - Unknown

Poster 3 - “If you are not willing to learn, no one can help you. If you are determined to learn, no one can stop you.”
- Unknown

NOTE: these posters should be designed as 18" X 24" in size with 2 of them being landscape and one being portrait orientation (as shown in images provided below)

Below are some sample images to give an idea on what could be used as background design for each quote. The logo that should be used as a watermark in a corner for some subtle branding has been provided as well.

Target Market(s)

The target market for this series are truck drivers between the ages of 25-55. Mostly males.

Industry/Entity Type

Landscape

Requirements
Must have
• Quote featured, high quality background design/image, logo watermark

```html
<!DOCTYPE html>
<html lang="en">
<head>
<meta charset="utf-8">
<title>Success Poster — Roadmark Driver Training</title>
<link rel="stylesheet" href="https://fonts.googleapis.com/css2?family=Montserrat:wght@300;400;600&display=swap">
<style>
  :root {
    --page: #ffffff;
    --sky-deep: #1b3f5e;
    --sky-mid: #3f79a8;
    --sky-light: #9cc3e0;
    --horizon: #c9dced;
    --ground: #4a3a2c;
    --road: #3a3b3d;
    --road-dark: #2a2a2b;
    --text-light: #ffffff;
    --accent-yellow: #f2e51b;
  }
  html, body {
    margin: 0;
    padding: 0;
    width: 1200px;
    height: 900px;
    overflow: hidden;
    background: var(--page);
  }
  .poster {
    position: absolute;
    left: 148px;
    top: 110px;
    width: 905px;
    height: 681px;
    overflow: hidden;
    font-family: "Montserrat", sans-serif;
    color: var(--text-light);
  }
  .poster__backdrop {
    position: absolute;
    inset: 0;
    background: linear-gradient(
      to bottom,
      var(--sky-deep) 0%,
      var(--sky-mid) 30%,
      var(--sky-light) 58%,
      var(--horizon) 66%,
      var(--ground) 70%,
      var(--ground) 74%,
      var(--road) 80%,
      var(--road-dark) 100%
    );
  }
  .quote {
    position: absolute;
    margin: 0;
    font-weight: 300;
    font-size: 54px;
    line-height: 56px;
    letter-spacing: -1px;
    text-transform: uppercase;
  }
  .quote--opening {
    left: 80px;
    top: 48px;
  }
  .quote__mark {
    position: absolute;
    left: -28px;
    top: 0;
  }
  .quote--closing {
    right: 51px;
    top: 320px;
    text-align: right;
  }
  .quote__highlight {
    display: block;
    color: var(--accent-yellow);
  }
  .attribution {
    position: absolute;
    right: 51px;
    top: 487px;
    margin: 0;
    font-weight: 400;
    font-size: 22px;
  }
  .brand {
    position: absolute;
    left: 73px;
    top: 598px;
    display: flex;
    align-items: center;
    gap: 10px;
    font-weight: 600;
    font-size: 20px;
    line-height: 1;
  }
  .brand__square {
    width: 30px;
    height: 30px;
    background: var(--text-light);
  }
</style>
</head>
<body>
  <main class="poster">
    <div class="poster__backdrop" role="img" aria-label="Photo of a white semi truck driving along a desert highway under a deep blue sky"></div>

    <p class="quote quote--opening"><span class="quote__mark">“</span>Success doesn’t<br>just come and<br>find you,</p>

    <p class="quote quote--closing">You have to<span class="quote__highlight">go out and<br>get it.”</span></p>

    <p class="attribution">- Unknown</p>

    <div class="brand">
      <span class="brand__square"></span>
      <span class="brand__name">Roadmark Driver Training</span>
    </div>
  </main>
</body>
</html>
```